Business Card Design Project

Business Card
We are rebranding with a new logo
Industry/Entity Type
Business
Contact Information for Business Card
Dennis Marlow +61 427581962 dennis@qovo.com.au P.O. Box 872 Kelvindale QLD 4309
Requirements
Must have
- Logo

```html
<!DOCTYPE html>
<html lang="en">
<head>
<meta charset="utf-8">
<title>Qovo International – Business Card</title>
<link rel="stylesheet" href="https://fonts.googleapis.com/css2?family=Open+Sans:wght@400;600;700&display=swap">
<style>
  :root {
    --orange: #f7941d;
    --navy: #004e6e;
    --sky: #1a9ad6;
    --white: #ffffff;
    --paper: #ffffff;
  }
  html, body {
    margin: 0;
    padding: 0;
    width: 1200px;
    height: 720px;
    overflow: hidden;
    background: var(--paper);
  }
  .card {
    position: relative;
    width: 1200px;
    height: 720px;
    background: var(--paper);
    font-family: "Open Sans", Arial, sans-serif;
    overflow: hidden;
  }
  .card-shapes {
    position: absolute;
    inset: 0;
  }
  .brand {
    position: absolute;
    left: 740px;
    top: 210px;
    display: flex;
    align-items: center;
    gap: 18px;
  }
  .brand-dot {
    width: 34px;
    height: 34px;
    border-radius: 50%;
    background: var(--sky);
  }
  .brand-name {
    font-weight: 700;
    font-size: 40px;
    letter-spacing: 4px;
    color: var(--navy);
    text-transform: uppercase;
    line-height: 1;
  }
  .holder {
    position: absolute;
    left: 99px;
    top: 362px;
    display: flex;
    align-items: center;
    gap: 32px;
  }
  .holder-bar {
    width: 4px;
    height: 58px;
    background: var(--white);
  }
  .holder-name {
    font-size: 54px;
    font-weight: 400;
    color: var(--white);
    line-height: 1;
    letter-spacing: 0.5px;
  }
  .contact {
    position: absolute;
    display: flex;
    align-items: center;
    color: var(--white);
    font-size: 29px;
    line-height: 1;
  }
  .contact svg { flex: none; }
  .contact-email { left: 45px; top: 522px; gap: 22px; }
  .contact-phone { left: 455px; top: 530px; gap: 16px; }
  .contact-address { left: 180px; top: 604px; gap: 18px; font-size: 25px; }
</style>
</head>
<body>
<div class="card">
  <svg class="card-shapes" width="1200" height="720" viewBox="0 0 1200 720" aria-hidden="true">
    <path d="M-20 437 L811 437 L777 693 L-20 693 Z" fill="var(--navy)" stroke="var(--navy)" stroke-width="16" stroke-linejoin="round"/>
    <path d="M-20 320 L597 320 L572 469 L-20 469 Z" fill="var(--orange)" stroke="var(--orange)" stroke-width="16" stroke-linejoin="round"/>
    <path d="M1045 462 L1220 462 L1220 693 L1100 693 Z" fill="var(--orange)" stroke="var(--orange)" stroke-width="16" stroke-linejoin="round"/>
  </svg>

  <div class="brand">
    <span class="brand-dot"></span>
    <span class="brand-name">Qovo International</span>
  </div>

  <div class="holder">
    <span class="holder-bar"></span>
    <span class="holder-name">Dennis Marlow</span>
  </div>

  <div class="contact contact-email">
    <svg width="38" height="38" viewBox="0 0 38 38" aria-hidden="true">
      <circle cx="19" cy="19" r="19" fill="var(--white)"/>
      <path d="M10 14 L19 20 L28 14 L28 26 L10 26 Z" fill="var(--navy)"/>
      <path d="M10 12.5 L28 12.5 L19 18.5 Z" fill="var(--navy)"/>
    </svg>
    <span>dennis@qovo.com.au</span>
  </div>

  <div class="contact contact-phone">
    <svg width="36" height="36" viewBox="0 0 36 36" aria-hidden="true">
      <circle cx="18" cy="18" r="18" fill="var(--white)"/>
      <path d="M12 9 C11 9 9 11 9 13 C9 20 16 27 23 27 C25 27 27 25 27 24 L27 22 L22.5 20 L20.5 22 C17.5 20.8 15.2 18.5 14 15.5 L16 13.5 L14 9 Z" fill="var(--navy)"/>
    </svg>
    <span>+61 427581962</span>
  </div>

  <div class="contact contact-address">
    <svg width="34" height="34" viewBox="0 0 34 34" aria-hidden="true">
      <circle cx="17" cy="17" r="17" fill="var(--white)"/>
      <path d="M17 7 C12.6 7 10 10 10 13.6 C10 18.5 17 26 17 26 C17 26 24 18.5 24 13.6 C24 10 21.4 7 17 7 Z" fill="var(--navy)"/>
      <circle cx="17" cy="13.8" r="3" fill="var(--white)"/>
    </svg>
    <span>P.O. Box 872 Kelvindale QLD 4309</span>
  </div>
</div>
</body>
</html>
```